Distinctinctive and nordic inspired container design for a new started health and active brand.

Our company name is MORO and stands for "Move onward, Reach Outward". Our goal is to provide a no BS approach to Supplementation and specific problem solving products.

As a Danish based brand our key words is: "Minimalism", "clear lines", "Nordic colours i.eg. and as seen in canvas", "Purity", "simplicity", "design", "Functionality", "health", "clarity" and "calm".

This design is aimed at a two container product (AM) for "night" and (PM) for "day".
Design is focused on a rectangular shape with a rectangular shape lid that screws on to a uniform and harmonious design.
Colour wise we are most into matte "earth colors that can also be seen in canvas.
These can be singular or a mix in the design but we kindly ask to stay away from "bright and shiny" colours.
Logos and scriptures will be added as a 2D effect, with exception for the lid logo which we would to see retracted into the lid itself.

In a rendering design we would like two containers next to each other seen from different angles where one lid is screwed off and one is screwed on.
In addition we would like a single container rendering showing only PM and only AM.

Happy designing

Pieter & Rasmus - MORO

Target Market(s)

European and North american markets.
Target: Male and Female age group 18-50.

Industry/Entity Type

Health Product

Font styles to use
Serif
Sans Serif

Requirements
Must have
• Clear and distinctive profile
Matte colours
uniform and harmonious shape (rectangular base)
inspired by earth minerals colours and contours.
Nice to have
• 3D visual effect in rendering to better get a feel of the product
Should not have
• Shiny colours or material indicators.

```html
<!DOCTYPE html>
<html lang="en">
<head>
<meta charset="utf-8">
<title>MORO container range</title>
<link rel="stylesheet" href="https://fonts.googleapis.com/css2?family=Arimo:ital,wght@0,400;0,700;1,400&display=swap">
<style>
:root{
  --page:#ffffff;
  --body:#2b2d2d;
  --body-edge:#1f2121;
  --cap:#2a2c2c;
  --neck:#e4e8ea;
  --neck-line:#b9c0c4;
  --ink:#f2f2f2;
  --label:#ffffff;
  --label-ink:#111111;
  --panel-top:#1c2a55;
  --panel-bottom:#ffffff;
  --lid-grey:#4b4e50;
}
*{margin:0;padding:0;box-sizing:border-box}
html,body{width:1200px;height:833px;overflow:hidden;background:var(--page)}
body{position:relative;font-family:"Arimo",Arial,sans-serif}
.bottle{position:absolute;top:42px;width:254px;height:745px}
.bottle--facts{left:32px}
.bottle--brand{left:323px}
.bottle--open{left:615px}
.cap{position:absolute;left:51px;top:0;width:152px;height:95px;background:var(--cap);border-radius:8px 8px 3px 3px;display:flex;align-items:center;justify-content:center;color:var(--ink);font-weight:700;font-size:26px;letter-spacing:.5px}
.neck{position:absolute;left:42px;top:95px;width:170px;height:34px;background:linear-gradient(var(--neck),#f6f8f9 50%,var(--neck));border-left:1px solid var(--neck-line);border-right:1px solid var(--neck-line)}
.threads{position:absolute;left:76px;top:18px;width:102px;height:111px;background:repeating-linear-gradient(172deg,#f4f6f7 0 10px,#cfd5d8 10px 12px);border:1px solid var(--neck-line);border-radius:3px}
.body{position:absolute;left:0;top:129px;width:254px;height:616px;background:linear-gradient(90deg,var(--body-edge),var(--body) 6%,var(--body) 94%,var(--body-edge));border-radius:6px}
.wordmark{position:absolute;left:0;width:100%;text-align:center;color:var(--ink);font-weight:700;font-size:30px;letter-spacing:4px}
.facts{position:absolute;left:35px;top:231px;width:193px;height:249px;background:var(--label);color:var(--label-ink);padding:4px 4px 3px;font-size:5.6px;line-height:1.18}
.facts h2{font-size:10px;line-height:1.1;border-bottom:.5px solid #000}
.facts table{width:100%;border-collapse:collapse;margin-top:1px}
.facts th{font-weight:700;text-align:right;border-bottom:2px solid #000;padding-bottom:1px}
.facts th:first-child{text-align:left}
.facts td{border-bottom:.4px solid #777;padding:.3px 0}
.facts td+td{text-align:right}
.facts tr.last td{border-top:2px solid #000}
.facts .note{margin-top:2px}
.emblem{position:absolute;left:48px;top:80px;width:146px;height:96px;border-radius:40% 40% 45% 45%;background:radial-gradient(ellipse at center,#d9d9d9 0,#9a9b9b 55%,var(--body) 100%)}
.vertical-name{position:absolute;left:127px;top:440px;transform:translate(-50%,-50%) rotate(-90deg);color:var(--ink);font-weight:700;font-size:62px;letter-spacing:18px;white-space:nowrap}
.vertical-square{position:absolute;left:112px;top:232px;width:30px;height:30px;border:3px solid var(--ink)}
.purpose{position:absolute;left:0;top:210px;width:100%;text-align:center;color:var(--ink);font-weight:700;font-size:15px}
.copy{position:absolute;left:46px;top:248px;width:192px;color:var(--ink);font-weight:700;font-size:8.6px;line-height:1.24}
.copy .big{float:left;font-style:italic;font-weight:400;font-size:30px;line-height:.95;margin-right:6px}
.lid-panel{position:absolute;left:888px;top:354px;width:302px;height:217px;background:linear-gradient(var(--panel-top),#5b6b8e 45%,var(--panel-bottom))}
.lid-round{position:absolute;left:17px;top:42px;width:124px;height:124px;border-radius:50%;background:var(--lid-grey);border:2px solid #6a6d70}
.lid-round .emblem-small{position:absolute;left:32px;top:16px;width:60px;height:48px;border-radius:40%;background:radial-gradient(#d6d6d6,#8d8f90 70%,var(--lid-grey))}
.lid-round span,.lid-flat{color:var(--ink);font-weight:700}
.lid-round span{position:absolute;left:0;top:74px;width:100%;text-align:center;font-size:19px}
.lid-flat{position:absolute;left:149px;top:79px;width:150px;height:84px;background:repeating-linear-gradient(90deg,#3e4143 0 3px,var(--lid-grey) 3px 5px);border-radius:4px;display:flex;align-items:center;justify-content:center;font-size:20px;padding-bottom:20px}
</style>
</head>
<body>
<div class="bottle bottle--facts">
  <div class="neck"></div><div class="cap"></div>
  <div class="body">
    <div class="wordmark" style="top:136px">MORO</div>
    <div class="facts">
      <h2>Supplement Facts</h2>
      <div>Serving Size: One tablet</div>
      <table>
        <tr><th></th><th>Amount Per Serving</th><th>% Daily Value</th></tr>
        <tr><td>Vitamin A (14% as beta-carotene)</td><td>3500 IU</td><td>70%</td></tr>
        <tr><td>Vitamin C</td><td>60 mg</td><td>100%</td></tr>
        <tr><td>Vitamin D (as Vitamin D3)</td><td>700 IU</td><td>175%</td></tr>
        <tr><td>Vitamin E</td><td>22.5 IU</td><td>75%</td></tr>
        <tr><td>Vitamin K</td><td>20 mcg</td><td>25%</td></tr>
        <tr><td>Thiamin (B1)</td><td>1.35 mg</td><td>90%</td></tr>
        <tr><td>Riboflavin (B2)</td><td>1.7 mg</td><td>100%</td></tr>
        <tr><td>Niacin</td><td>18 mg</td><td>90%</td></tr>
        <tr><td>Vitamin B6</td><td>3 mg</td><td>150%</td></tr>
        <tr><td>Folic Acid</td><td>400 mcg</td><td>100%</td></tr>
        <tr><td>Vitamin B12</td><td>18 mcg</td><td>300%</td></tr>
        <tr><td>Biotin</td><td>75 mcg</td><td>25%</td></tr>
        <tr><td>Pantothenic Acid</td><td>16 mg</td><td>160%</td></tr>
        <tr><td>Calcium (elemental)</td><td>210 mg</td><td>21%</td></tr>
        <tr><td>Iron</td><td>0 mg</td><td>0%</td></tr>
        <tr><td>Magnesium</td><td>140 mg</td><td>35%</td></tr>
        <tr><td>Zinc</td><td>15 mg</td><td>100%</td></tr>
        <tr><td>Selenium</td><td>110 mcg</td><td>157%</td></tr>
        <tr><td>Copper</td><td>2 mg</td><td>100%</td></tr>
        <tr><td>Manganese</td><td>2 mg</td><td>100%</td></tr>
        <tr><td>Chromium</td><td>120 mcg</td><td>100%</td></tr>
        <tr class="last"><td>Lycopene</td><td>300 mcg</td><td>*</td></tr>
      </table>
      <div class="note">*Daily Value not established.</div>
    </div>
  </div>
</div>

<div class="bottle bottle--brand">
  <div class="neck"></div><div class="cap">MALE</div>
  <div class="body">
    <div class="emblem" role="img" aria-label="Crescent moon among swirling clouds emblem"></div>
    <div class="vertical-square"></div>
    <div class="vertical-name">MORO</div>
  </div>
</div>

<div class="bottle bottle--open">
  <div class="neck"></div><div class="threads"></div>
  <div class="body">
    <div class="wordmark" style="top:162px">MORO</div>
    <div class="purpose">PURPOSE</div>
    <p class="copy"><span class="big">99%</span>Lorem ipsum dolor sit amet, consec tetur adipiscing elit. Morbi ultricies molestie orci. Aenean purus mauris, sodales nec diam dignissim, porttitor laoreet enim. Aliquam id sollicitudin turpis. Vivamus aliquet elit sem, et ornare ex aliquam in. In cursus, felis non pretium molestie, tellus lacus facilisis metus, ut accumsan nisi nulla accumsan risus. Etiam id pharetra ante. Nunc sit amet ante id justo consequat tempor. Nullam pretium arcu eu hendrerit aliquam. Sed in purus eros.</p>
  </div>
</div>

<div class="lid-panel">
  <div class="lid-round"><div class="emblem-small" role="img" aria-label="Moon and clouds emblem recessed into lid"></div><span>PM</span></div>
  <div class="lid-flat">MALE</div>
</div>
</body>
</html>
```